依頼詳細
専門ひだまり便もスタートしたので、名刺を新しく作り直そうと思っております。
ひだまり便事業部の中に【家族ひだまり便】と【専門ひだまり便】というターゲットが違う仕事をしているだけで、対応するメンバーは、変わらないので、名刺を一枚にまとめたいと考えています。
両方のチラシを添付しておりますし、ホームページもあります。
全員で7名分作成のお願いが出来たらと思います。
記載項目は入れたいと思っております。それ以外は、お任せいたします。

宜しくお願いいたします。
記載項目
表面:会社名、住所、電話番号、FAX、メールアドレス、個人の資格、名前と役職、似顔絵
裏面:家族ひだまり便の事業内容・不用品回収、遺品整理、生前整理、住まいのお困り事対応サービス
専門ひだまり便の事業内容・弁護士、司法書士、税理士などの士業専門の不用品回収や遺品整理、機密文書処理
会社の資格:北九州市一廃廃棄物収集運搬許可 北九一廃第382号
希望イメージ
シンプル 複雑
単色 カラフル
暗い 明るい
日常 高級
遊び心 厳粛
未来的 伝統的
女性的 男性的
希望する色
緑系、青系、水色系
納品ファイル
• 高解像度JPG (.jpg)
• イラストレーター形式 (.ai)
• PNG形式 (.png)
補足説明
会社の許可の部分で、あと2つ許可を追加していただけたらと思います。
産業廃棄物処分業許可 第05213384720号
産業廃棄物収集運搬業 06281937402
上記2点です。
宜しくお願いいたします。
■ 選んだ理由

シンプルかつ私がイメージしていた名刺のデザインだったため、選ばせていただきました。

■ 提案者全員のお礼・コメント

色々と提案していただき、ありがとうございました。
どれにするかとても迷うぐらい良い物ばかりでした。
今後とも宜しくお願いいたします。

```html
<!DOCTYPE html>
<html lang="ja">
<head>
<meta charset="UTF-8">
<title>名刺 表面・裏面</title>
<link href="https://fonts.googleapis.com/css2?family=Noto+Sans+JP:wght@400;500;700&display=swap" rel="stylesheet">
<style>
  :root {
    --page: #f4f4f4;
    --card: #ffffff;
    --panel: #ececec;
    --green: #5bb431;
    --blue: #1c8dd0;
    --ink: #333333;
    --muted: #777777;
    --portrait: #d9c6b0;
  }
  * { box-sizing: border-box; margin: 0; padding: 0; }
  html, body { width: 847px; height: 1200px; overflow: hidden; }
  body {
    background: var(--page);
    font-family: "Noto Sans JP", sans-serif;
    color: var(--ink);
    position: relative;
  }
  .card {
    position: absolute;
    left: 62px;
    width: 723px;
    height: 480px;
    background: var(--card);
    box-shadow: 0 3px 10px rgba(0,0,0,0.25);
    overflow: hidden;
  }
  .card--front { top: 70px; }
  .card--back { top: 620px; }
  .abs { position: absolute; }

  /* front */
  .profile-panel { left: 0; top: 0; width: 470px; height: 262px; background: var(--panel); }
  .rule-blue { left: 0; top: 262px; width: 470px; height: 4px; background: var(--blue); }
  .rule-green-v { left: 470px; top: 0; width: 5px; height: 480px; background: var(--green); }
  .rule-top-right { left: 475px; top: 0; width: 248px; height: 6px; background: var(--blue); }
  .portrait { left: 28px; top: 34px; width: 130px; height: 130px; border-radius: 50%; background: radial-gradient(circle at 50% 40%, #e8d6c2, var(--portrait)); }
  .credential { left: 28px; top: 178px; font-size: 12px; color: var(--muted); }
  .role { left: 250px; top: 48px; font-size: 14px; }
  .name { left: 228px; top: 72px; font-size: 44px; font-weight: 700; letter-spacing: 6px; }
  .name-roman { left: 246px; top: 140px; font-size: 15px; font-style: italic; color: var(--muted); }
  .company { left: 28px; top: 288px; font-size: 24px; font-weight: 700; }
  .contact { left: 28px; top: 330px; font-size: 15px; line-height: 26px; }
  .contact span + span { margin-left: 22px; }

  .brand { display: flex; align-items: center; gap: 10px; font-size: 26px; font-weight: 700; }
  .brand__mark { width: 22px; height: 22px; }
  .brand--green { color: var(--green); }
  .brand--green .brand__mark { background: var(--green); }
  .brand--blue { color: var(--blue); }
  .brand--blue .brand__mark { background: var(--blue); }
  .front-brand { left: 475px; width: 248px; justify-content: center; }
  .front-brand--1 { top: 105px; }
  .front-brand--2 { top: 270px; }

  /* back */
  .license-title { left: 40px; top: 40px; font-size: 18px; font-weight: 500; }
  .license-list { left: 330px; top: 26px; font-size: 13px; line-height: 28px; list-style: none; }
  .license-list li::before { content: "■"; color: var(--green); margin-right: 6px; font-size: 10px; }
  .rule-green-h { left: 0; top: 124px; width: 723px; height: 5px; background: var(--green); }
  .divider { left: 361px; top: 150px; height: 300px; border-left: 2px dashed #bbbbbb; }
  .service { top: 170px; width: 361px; padding: 0 40px; }
  .service--family { left: 0; }
  .service--pro { left: 362px; }
  .service .brand { justify-content: center; height: 90px; }
  .service__heading { margin-top: 24px; font-size: 20px; font-weight: 700; }
  .service__text { margin-top: 10px; font-size: 16px; line-height: 28px; }
  .service--family .service__heading, .service--family .service__text { color: var(--green); }
  .service--pro .service__heading, .service--pro .service__text { color: var(--blue); }
</style>
</head>
<body>

<section class="card card--front">
  <div class="abs profile-panel"></div>
  <div class="abs rule-blue"></div>
  <div class="abs rule-green-v"></div>
  <div class="abs rule-top-right"></div>
  <div class="abs portrait" role="img" aria-label="代表取締役の似顔絵イラスト"></div>
  <p class="abs credential">資格 ○○○○○○</p>
  <p class="abs role">代表取締役</p>
  <p class="abs name">森田 健一</p>
  <p class="abs name-roman">Kenichi Morita</p>
  <p class="abs company">株式会社ミドリノ</p>
  <div class="abs contact">
    <p>〒800-0000 北九州市門司区青葉町1-2-3</p>
    <p><span>Tel. 093-000-1234</span><span>Fax. 093-000-5678</span></p>
    <p>E-mail. info@hidamaribin.example</p>
    <p>URL. https://hidamaribin.example</p>
  </div>
  <div class="abs brand brand--green front-brand front-brand--1"><span class="brand__mark"></span>家族ひだまり便</div>
  <div class="abs brand brand--blue front-brand front-brand--2"><span class="brand__mark"></span>専門ひだまり便</div>
</section>

<section class="card card--back">
  <p class="abs license-title">【会社の資格】</p>
  <ul class="abs license-list">
    <li>北九州市一廃廃棄物収集運搬許可 北九一廃第382号</li>
    <li>産業廃棄物処分業許可 第05213384720号</li>
    <li>産業廃棄物収集運搬業 06281937402</li>
  </ul>
  <div class="abs rule-green-h"></div>
  <div class="abs divider"></div>
  <div class="abs service service--family">
    <div class="brand brand--green"><span class="brand__mark"></span>家族ひだまり便</div>
    <p class="service__heading">【事業内容】</p>
    <p class="service__text">不用品回収、遺品整理、生前整理、住まいのお困り事対応サービス</p>
  </div>
  <div class="abs service service--pro">
    <div class="brand brand--blue"><span class="brand__mark"></span>専門ひだまり便</div>
    <p class="service__heading">【事業内容】</p>
    <p class="service__text">弁護士、司法書士、税理士などの士業専門の不用品回収や遺品整理、機密文書処理</p>
  </div>
</section>

</body>
</html>
```